HVAC company business card design

We need a business card design for a HVAC company. The design must look professional. Both sides will be used. The total data to be on the business card is
Name
Position
Email
Direct Phone/Moile Phone
Company Contacts /Address, Phone, Fax, web)
All data will be submit once the design is confirmed. For generic purposes use;
Emre Toksoy
Managing Director
+902324815263 (Mobile)
4712 Sokak No: 9 KBSE Yenikent IZMIR TURKEY
Tel: +902324815263 Fax : +902324815269
www.luvon.com.tr

Target Market(s)

HVAC

Industry/Entity Type

Business

Contact Information for Business Card

The total data to be on the business card is
Name
Position
Email
Direct Phone/Moile Phone
Emre Toksoy
Managing Director
+902324815263 (Mobile)
www.luvon.com.tr
The BC will use both sides of the card. The front will include the full logo and the details for the business card holder. The business card can be divided into vertical/horizontal or to a special shape. The common data like the company address/phone/fax should be indicated elsewehere. The back can contain some part or the whole logo and must contain the web address.

Font styles to use
Serif
Sans Serif

Colors
0355a3
cfdfed

Requirements
Should not have
• Please be careful with the fonts, it shouldnt be too small or too big and must not interfere with the logo fonts. If you need to use a curvy shape please do not use as the logo is already curvy or use the curves from the logo (if it looks good, otherwise forget it)
• We are not in favor of pictograms, only if they are perfect use them.

```html
<!DOCTYPE html>
<html lang="en">
<head>
<meta charset="utf-8">
<title>Luvon – Business Card</title>
<link rel="stylesheet" href="https://fonts.googleapis.com/css2?family=Open+Sans:wght@400;600&display=swap">
<style>
  :root {
    --backdrop: #262626;
    --navy: #3e4964;
    --brand-blue: #3a6fc0;
    --brand-blue-light: #4f96dc;
    --silver: #d9dde4;
    --silver-band: #a9adb4;
    --silver-band-light: #c2c6cc;
    --ink: #2f3440;
    --logo-grey: #d5d8de;
  }
  * { margin: 0; padding: 0; box-sizing: border-box; }
  html, body { width: 1200px; height: 1200px; overflow: hidden; }
  body {
    background: var(--backdrop);
    font-family: "Open Sans", sans-serif;
    position: relative;
  }
  .card {
    position: absolute;
    width: 680px;
    height: 390px;
    border-radius: 22px;
    overflow: hidden;
  }
  /* Back side */
  .card-back {
    left: 110px;
    top: 170px;
    background: var(--navy);
  }
  .card-back .brand-disc {
    position: absolute;
    right: -70px;
    top: 40px;
    width: 340px;
    height: 340px;
    border-radius: 50%;
    background: radial-gradient(circle at 40% 40%, #55648a, #45527a 70%);
  }
  .card-back .brand-block {
    position: absolute;
    left: 90px;
    top: 150px;
  }
  .card-back .brand-name {
    font-size: 80px;
    font-weight: 600;
    letter-spacing: 4px;
    line-height: 1;
    color: var(--logo-grey);
  }
  .card-back .web-address {
    margin-top: 10px;
    margin-left: 6px;
    font-size: 26px;
    font-weight: 400;
    letter-spacing: 1px;
    color: var(--brand-blue);
  }
  /* Front side */
  .card-front {
    left: 410px;
    top: 640px;
    background: radial-gradient(circle at 62% 55%, #e6e9f0, var(--silver) 70%);
  }
  .card-front .bands { position: absolute; inset: 0; }
  .brand-lockup {
    position: absolute;
    right: 44px;
    top: 60px;
    display: flex;
    align-items: center;
    gap: 16px;
  }
  .brand-lockup .brand-dot {
    width: 64px;
    height: 64px;
    border-radius: 50%;
    background: var(--brand-blue);
  }
  .brand-lockup .brand-name {
    font-size: 70px;
    font-weight: 600;
    letter-spacing: 3px;
    color: var(--ink);
    line-height: 1;
  }
  .holder {
    position: absolute;
    right: 44px;
    top: 170px;
    text-align: right;
  }
  .holder .person-name {
    font-size: 24px;
    font-weight: 400;
    letter-spacing: 1px;
    color: var(--ink);
    text-transform: uppercase;
  }
  .holder .person-role {
    font-size: 17px;
    color: var(--brand-blue);
    margin-top: -2px;
  }
  .contact-lines {
    list-style: none;
    margin-top: 10px;
  }
  .contact-lines li {
    display: flex;
    justify-content: flex-end;
    align-items: center;
    gap: 8px;
    font-size: 17px;
    color: var(--brand-blue);
    line-height: 24px;
  }
  .contact-lines svg { width: 16px; height: 16px; }
  .address {
    margin-top: 18px;
    font-size: 16px;
    font-weight: 600;
    letter-spacing: 0.5px;
    color: var(--ink);
    line-height: 22px;
  }
</style>
</head>
<body>
  <section class="card card-back" aria-label="Card back">
    <div class="brand-disc" role="img" aria-label="Soft brand decoration area"></div>
    <div class="brand-block">
      <div class="brand-name">LUVON</div>
      <div class="web-address">www.luvon.com.tr</div>
    </div>
  </section>

  <section class="card card-front" aria-label="Card front">
    <svg class="bands" viewBox="0 0 680 390" preserveAspectRatio="none" aria-hidden="true">
      <path d="M300 0 H336 C246 120 206 260 236 390 H180 C150 260 200 120 300 0 Z" fill="var(--silver-band-light)"/>
      <path d="M230 0 H300 C200 120 150 260 180 390 H40 C60 230 130 90 230 0 Z" fill="var(--silver-band)"/>
      <path d="M0 0 H230 C130 90 60 230 40 390 H0 Z" fill="var(--brand-blue)"/>
      <path d="M0 0 H70 C40 50 15 110 0 160 Z" fill="var(--brand-blue-light)"/>
    </svg>

    <div class="brand-lockup">
      <span class="brand-dot"></span>
      <span class="brand-name">LUVON</span>
    </div>

    <div class="holder">
      <p class="person-name">Emre Toksoy</p>
      <p class="person-role">Managing Director</p>
      <ul class="contact-lines">
        <li>+902324815263
          <svg viewBox="0 0 16 16"><circle cx="8" cy="8" r="8" fill="var(--ink)"/><rect x="5.5" y="3.5" width="5" height="9" rx="1" fill="none" stroke="#fff" stroke-width="1.2"/></svg>
        </li>
        <li>+902324815263
          <svg viewBox="0 0 16 16"><circle cx="8" cy="8" r="8" fill="var(--ink)"/><path d="M5 4 L7 4 L7.6 6 L6.5 7 C7 8.3 7.8 9 9 9.5 L10 8.4 L12 9 L12 11 C8 11.5 4.5 8 5 4 Z" fill="#fff"/></svg>
        </li>
        <li>+902324815269
          <svg viewBox="0 0 16 16"><circle cx="8" cy="8" r="8" fill="var(--ink)"/><rect x="4" y="7" width="8" height="5" rx="1" fill="#fff"/><rect x="5.5" y="4" width="5" height="3" fill="none" stroke="#fff" stroke-width="1"/></svg>
        </li>
      </ul>
      <p class="address">4712 SOKAK<br>No: 9 KBSE YENIKENT IZMIR TURKEY</p>
    </div>
  </section>
</body>
</html>
```